Creative label for amber glass candle jar.

We are a candle company. Our products are handmade by us and natural. We are looking for something minimalistic and unique. We need a label for our candle jars (amber glass with black lid). Our current label doesn't match these requirements. We would like our products to be stocked in London shop, therefore design has to be up to a high standard. Jar specification Diameter (mm) 65 Height without cap (mm) 80. We want the new design to be different from the current one. It's just a guide for wording.
We should be able adjust the label, to change scent name.
Our scents are
*Coconut & Vanilla
*Lavender
*Bergamot
*Italian Garden
*Hygge
*Eucalyptus & Peppermint
*Coffee
*Cedarwood & Juniperberry
To know more about us, visit our website www.wrenfieldcandles.com or instagram.com/wrenfieldcandles
Good luck!
Industry/Entity Type
It Company
Colors
Designer to choose colors to be used in the design.
Requirements
Must have
- * I have attached two of our logos, label design must include one of them.
- *has to mention that it's made in London
- *has to say that candle is natural/made with essential oils
- *has to have scent name and No. on it..
- Label can be vertical or horizontal, but has to be square/rectangular,.
Should not have
- Label should not be round

```html
<!DOCTYPE html>
<html lang="en">
<head>
<meta charset="utf-8">
<title>Wrenfield Candles – No 8 Cedarwood &amp; Juniperberry Label</title>
<link href="https://fonts.googleapis.com/css2?family=Great+Vibes&family=Delius+Unicase&family=Open+Sans+Condensed:wght@300&family=Open+Sans:wght@400&display=swap" rel="stylesheet">
<style>
  :root {
    --backdrop: #e8e8e8;
    --label: #232527;
    --ink: #e4e4e2;
    --teal: #2f8c82;
    --teal-deep: #3c7478;
  }
  * { margin: 0; padding: 0; box-sizing: border-box; }
  html, body {
    width: 1200px;
    height: 1200px;
    overflow: hidden;
    background: var(--backdrop);
  }
  .label {
    position: absolute;
    left: 292px;
    top: 100px;
    width: 616px;
    height: 1000px;
    background: var(--label);
    color: var(--ink);
  }
  .label__frame {
    position: absolute;
    inset: 0;
  }
  .label__number {
    position: absolute;
    top: 24px;
    right: 92px;
    font-family: "Open Sans", sans-serif;
    font-size: 34px;
    letter-spacing: 1px;
  }
  .label__brand {
    position: absolute;
    top: 118px;
    right: 62px;
    display: flex;
    align-items: center;
    gap: 12px;
    font-family: "Delius Unicase", sans-serif;
    font-size: 34px;
    color: var(--teal-deep);
  }
  .label__brand-mark {
    width: 18px;
    height: 18px;
    background: var(--teal-deep);
  }
  .scent {
    position: absolute;
    right: 50px;
    top: 355px;
    text-align: right;
    font-family: "Great Vibes", cursive;
    font-size: 96px;
    line-height: 1;
  }
  .scent__line { display: block; }
  .scent__amp { margin-right: -14px; line-height: 1.2; }
  .label__claims {
    position: absolute;
    right: 52px;
    top: 770px;
    text-align: right;
    font-family: "Delius Unicase", sans-serif;
    font-size: 28px;
    line-height: 1.3;
  }
  .label__origin {
    position: absolute;
    right: 58px;
    top: 878px;
    font-family: "Delius Unicase", sans-serif;
    font-size: 26px;
  }
</style>
</head>
<body>
  <div class="label">
    <svg class="label__frame" width="616" height="1000" viewBox="0 0 616 1000" aria-hidden="true">
      <path d="M592 28 V948 H128" fill="none" stroke="var(--teal)" stroke-width="3" stroke-dasharray="4 5"/>
    </svg>

    <div class="label__number">NO 8</div>

    <div class="label__brand">
      <span class="label__brand-mark"></span>
      <span>Wrenfield</span>
    </div>

    <h1 class="scent">
      <span class="scent__line">Cedarwood</span>
      <span class="scent__line scent__amp">&amp;</span>
      <span class="scent__line">Juniperberry</span>
    </h1>

    <p class="label__claims">100% natural soy wax candle<br>with essential oils</p>
    <p class="label__origin">made in London</p>
  </div>
</body>
</html>
```